Business Card Design Project

I am a Chiropractor that is looking for a new business card.  Our logo was slightly changed lately, therefore need a new, more professional look.
We are a modern, non-stuffy chiropractic office.  Want a contemporary look that will let people know this is not your typical doctors office.  Our logo is red, and contains the name of our business: realign.  The u in the logo is green, stressing the most important part of our business: "u"

Target Market(s)
moderate to upper income bracket, family friendly
www.realignspine-example.com
Gordon Pell
Family Chiropractor
314 Hollis Rd
Millbrook, OR 97999
541.555.0147 phone
541.555.0148 fax
Industry/Entity Type
Business
Requirements
Must have
- www.realignspine-example.com
Gordon Pell
Family Chiropractor
314 Hollis Rd
Millbrook, OR 97999
541.555.0147 phone
541.555.0148 fax

```html
<!DOCTYPE html>
<html lang="en">
<head>
<meta charset="utf-8">
<title>realign – Business Card</title>
<link rel="stylesheet" href="https://fonts.googleapis.com/css2?family=Open+Sans:wght@400;600&display=swap">
<style>
  :root {
    --page-bg: #ffffff;
    --card-bg: #ffffff;
    --card-border: #9a9a9a;
    --ink: #333336;
    --ink-soft: #3c3c3e;
    --lime-light: #e6f21a;
    --lime: #a6f01e;
    --green: #2ef01a;
  }
  html, body {
    margin: 0;
    padding: 0;
    width: 1200px;
    height: 900px;
    overflow: hidden;
    background: var(--page-bg);
    font-family: "Open Sans", Arial, sans-serif;
  }
  .canvas {
    position: relative;
    width: 1200px;
    height: 900px;
  }
  .business-card {
    position: absolute;
    left: 70px;
    top: 126px;
    width: 1056px;
    height: 644px;
    background: var(--card-bg);
    border: 2px solid var(--card-border);
  }
  .spine-motif {
    position: absolute;
    left: 136px;
    top: 8px;
    width: 160px;
    height: 632px;
  }
  .brand-name {
    position: absolute;
    left: 508px;
    top: 20px;
    margin: 0;
    font-size: 108px;
    font-weight: 400;
    letter-spacing: -2px;
    line-height: 1.3;
    color: var(--ink);
  }
  .practitioner {
    position: absolute;
    left: 512px;
    top: 270px;
    margin: 0;
    font-size: 28px;
    line-height: 38px;
    color: var(--ink-soft);
  }
  .contact {
    position: absolute;
    left: 512px;
    top: 482px;
    margin: 0;
    font-style: normal;
    font-size: 22px;
    line-height: 30px;
    color: var(--ink-soft);
  }
  .contact span { display: block; }
</style>
</head>
<body>
<main class="canvas">
  <section class="business-card">
    <svg class="spine-motif" viewBox="0 0 160 632" role="img" aria-label="Vertical spine motif of graded yellow-to-green dots">
      <defs>
        <linearGradient id="spineGradient" x1="0" y1="0" x2="0" y2="1">
          <stop offset="0" stop-color="var(--lime-light)" stop-opacity="0.55"/>
          <stop offset="0.5" stop-color="var(--lime)" stop-opacity="0.55"/>
          <stop offset="1" stop-color="var(--green)" stop-opacity="0.55"/>
        </linearGradient>
      </defs>
      <rect x="20" y="0" width="120" height="632" rx="60" fill="url(#spineGradient)"/>
    </svg>

    <h1 class="brand-name">realign</h1>

    <p class="practitioner">
      Gordon Pell<br>
      Family Chiropractor
    </p>

    <address class="contact">
      <span>314 Hollis Rd, Millbrook, OR 97999</span>
      <span>Phone 541.555.0147</span>
      <span>Fax 541.555.0148</span>
      <span>www.realignspine-example.com</span>
    </address>
  </section>
</main>
</body>
</html>
```